Green Smoothie Product Launch Graphics

I want to create 9-10 social media graphics (new Instagram size 4:5 (1080 x 1350 pixels) focusing on our new Leafy Blend Gummies Product launch. Use any of the attached pics in the Dropbox, NO RANDOM STOCK PHOTOGRAPHY. For the color scheme of the graphics, they should all be complementary to the green smoothie gummy product attached.
You can add any of the photos as they are all posted here. You do NOT need to access Dropbox now. (see WORD document for all details)
Updates

All of the images are now posted here. You do NOT need to access the Dropbox

Target Market(s)

women and men

Requirements
Must have
• all the text and pictures in the drobpx

```html
<!DOCTYPE html>
<html lang="en">
<head>
<meta charset="utf-8">
<title>Leafy Blend Gummies – Launch Social Set</title>
<link rel="stylesheet" href="https://fonts.googleapis.com/css2?family=Outfit:wght@500;600;700&display=swap">
<style>
:root{
  --green:#2d7e35;
  --green-deep:#1f5d24;
  --band:#357f3c;
  --mist:#e4eee6;
  --paper:#ffffff;
  --ring:#3f8c45;
}
*{margin:0;padding:0;box-sizing:border-box}
html,body{width:960px;height:1200px;overflow:hidden;background:var(--paper)}
body{position:relative;font-family:"Outfit",sans-serif;color:var(--green)}
.tile{position:absolute;width:282px;height:352px;overflow:hidden;
  background:linear-gradient(160deg,var(--mist) 0%,#f4f8f5 55%,var(--mist) 100%);
  box-shadow:0 14px 24px -12px rgba(0,0,0,.18)}
.col1{left:34px}.col2{left:341px}.col3{left:647px}
.row1{top:39px}.row2{top:425px}.row3{top:812px}
.txt{position:absolute;font-weight:600;letter-spacing:-.045em;white-space:nowrap}
.band{position:absolute;left:0;right:0;bottom:0;background:var(--band)}
.on-band{color:#fff}
.deep{color:var(--green-deep)}
.right{text-align:right}
.tm{font-size:.35em;vertical-align:top;line-height:1}
.rings{position:absolute;inset:0;width:282px;height:352px}
.rings circle{fill:none;stroke:var(--ring)}
.photo{position:absolute;border-radius:40% 40% 0 0}
.photo.person-pink{background:linear-gradient(180deg,#3a2a24 0%,#b98064 30%,#e3a2c4 60%,#d98fb8 100%)}
.photo.person-dots{background:linear-gradient(180deg,#2a201d 0%,#a8755c 30%,#2b2b2b 55%,#e6a8c8 100%)}
.photo.person-denim{background:linear-gradient(180deg,#4a3526 0%,#c99478 32%,#8fb3d9 60%,#6f95c4 100%)}
.photo.person-sport{background:linear-gradient(180deg,#2a1c16 0%,#7a4a32 35%,#4c6484 65%,#2f7a3a 100%)}
.bottle{position:absolute;border-radius:10px 10px 8px 8px;
  background:linear-gradient(180deg,#2f8a3a 0 9%,#5a3d2e 9% 22%,#f5f7f5 22% 100%)}
</style>
</head>
<body>

<!-- Row 1 -->
<section class="tile col1 row1">
  <svg class="rings" viewBox="0 0 282 352" aria-hidden="true">
    <circle cx="208" cy="326" r="62" stroke-width="2"/>
    <circle cx="208" cy="326" r="54" stroke-width="1"/>
  </svg>
  <div class="bottle" role="img" aria-label="Leafy Blend Gummies bottle with gummies" style="left:183px;top:254px;width:42px;height:81px"></div>
  <h1 class="txt" style="left:18px;top:18px;font-size:50px;line-height:38px">Introducing<br>Leafy<br>Blend<br>Gummies<span class="tm">™</span></h1>
  <p class="txt deep" style="left:18px;top:186px;font-size:32px;line-height:31px">Daily Supergreens<br>for Energy, Detox<br>and Glow</p>
</section>

<section class="tile col2 row1">
  <svg class="rings" viewBox="0 0 282 352" aria-hidden="true">
    <circle cx="141" cy="78" r="70" stroke-width="2"/>
    <circle cx="141" cy="78" r="60" stroke-width="1"/>
  </svg>
  <div class="photo person-pink" role="img" aria-label="Smiling woman in pink holding a gummy and the bottle" style="left:96px;top:22px;width:92px;height:120px"></div>
  <div class="band" style="top:142px"></div>
  <h2 class="txt on-band" style="left:15px;top:150px;font-size:46px;line-height:36px">Debloat,<br>Glow &amp;<br>Digest Better</h2>
  <p class="txt on-band" style="left:15px;top:272px;font-size:28px;line-height:27px">Mae’s&nbsp; Leafy Blend<br>Gummies</p>
</section>

<section class="tile col3 row1">
  <svg class="rings" viewBox="0 0 282 352" aria-hidden="true">
    <circle cx="205" cy="292" r="86" stroke-width="2"/>
    <circle cx="205" cy="292" r="76" stroke-width="1"/>
  </svg>
  <div class="photo person-sport" role="img" aria-label="Smiling woman in sports top holding the bottle" style="left:107px;top:190px;width:175px;height:162px"></div>
  <div class="bottle" role="img" aria-label="Leafy Blend Gummies bottle with gummies" style="left:31px;top:212px;width:81px;height:134px"></div>
  <h2 class="txt" style="left:21px;top:21px;font-size:38px;line-height:37px">Glow,<br>Feel Lighter &amp;<br>More Energized</h2>
  <p class="txt" style="left:21px;top:132px;font-size:30px;line-height:30px">in 2 Gummies a Day</p>
</section>

<!-- Row 2 -->
<section class="tile col1 row2">
  <svg class="rings" viewBox="0 0 282 352" aria-hidden="true">
    <circle cx="230" cy="300" r="82" stroke-width="2"/>
    <circle cx="230" cy="300" r="72" stroke-width="1"/>
  </svg>
  <div class="photo person-denim" role="img" aria-label="Smiling woman in denim jacket holding the bottle" style="left:156px;top:202px;width:126px;height:150px"></div>
  <h2 class="txt" style="left:17px;top:17px;font-size:55px;line-height:43px">Mae’s<br>Leafy<br>Blend<br>Gummies<span class="tm">™</span></h2>
  <p class="txt deep" style="left:17px;top:190px;font-size:55px;line-height:44px">Are<br>Here!</p>
</section>

<section class="tile col2 row2">
  <svg class="rings" viewBox="0 0 282 352" aria-hidden="true">
    <circle cx="146" cy="300" r="66" stroke-width="2"/>
    <circle cx="146" cy="300" r="56" stroke-width="1"/>
  </svg>
  <div class="bottle" role="img" aria-label="Leafy Blend Gummies bottle with gummies" style="left:118px;top:216px;width:56px;height:108px"></div>
  <h2 class="txt" style="left:16px;top:23px;font-size:51px;line-height:44px">No Time<br>to Blend ?</h2>
  <p class="txt right" style="right:13px;top:124px;font-size:31px;line-height:25px">Get That Leafy<br>Blend&nbsp; Feeling<br>in 2 Gummies a Day</p>
</section>

<section class="tile col3 row2">
  <svg class="rings" viewBox="0 0 282 352" aria-hidden="true">
    <circle cx="140" cy="78" r="70" stroke-width="2"/>
    <circle cx="140" cy="78" r="60" stroke-width="1"/>
  </svg>
  <div class="photo person-dots" role="img" aria-label="Smiling woman in polka-dot top pointing at the bottle" style="left:90px;top:8px;width:100px;height:134px"></div>
  <div class="band" style="top:142px"></div>
  <h2 class="txt on-band" style="left:16px;top:150px;font-size:46px;line-height:38px">Feel Like<br>You Did on<br>the Cleanse</h2>
  <p class="txt on-band" style="left:16px;top:268px;font-size:33px;line-height:29px">Without<br>The Prep or Mess</p>
</section>

<!-- Row 3 -->
<section class="tile col1 row3">
  <svg class="rings" viewBox="0 0 282 352" aria-hidden="true">
    <circle cx="149" cy="302" r="84" stroke-width="2"/>
    <circle cx="149" cy="302" r="74" stroke-width="1"/>
  </svg>
  <div class="photo person-dots" role="img" aria-label="Smiling woman in polka-dot top pointing at the bottle" style="left:98px;top:222px;width:102px;height:130px"></div>
  <h2 class="txt deep" style="left:20px;top:12px;font-size:43px;line-height:32px">Loved Mae’s<br>Cleanse?</h2>
  <p class="txt" style="left:20px;top:94px;font-size:46px;line-height:35px">Then You ‘ll<br>Loved These<br>Gummies</p>
</section>

<section class="tile col2 row3">
  <div class="band" style="top:206px"></div>
  <svg class="rings" viewBox="0 0 282 352" aria-hidden="true">
    <circle cx="215" cy="295" r="80" stroke-width="2"/>
    <circle cx="215" cy="295" r="70" stroke-width="1"/>
  </svg>
  <div class="bottle" role="img" aria-label="Leafy Blend Gummies bottle with gummies" style="left:168px;top:184px;width:76px;height:147px"></div>
  <h2 class="txt" style="left:18px;top:6px;font-size:57px;line-height:44px">Mae’s<br>Leafy<br>Blend<br>Cleanse</h2>
  <p class="txt on-band" style="left:17px;top:232px;font-size:41px;line-height:32px">Now in a<br>GUMMY</p>
</section>

<section class="tile col3 row3">
  <svg class="rings" viewBox="0 0 282 352" aria-hidden="true">
    <circle cx="144" cy="280" r="76" stroke-width="2"/>
    <circle cx="144" cy="280" r="66" stroke-width="1"/>
  </svg>
  <div class="photo person-pink" role="img" aria-label="Smiling woman in pink holding a gummy and the bottle" style="left:95px;top:214px;width:98px;height:138px"></div>
  <h2 class="txt" style="left:12px;top:20px;font-size:49px;line-height:38px">Get Your<br>Daily Greens</h2>
  <p class="txt deep right" style="right:15px;top:114px;font-size:40px;line-height:33px">No Blender<br>Just Gummies</p>
</section>

</body>
</html>
```